Plakat-Design für Zimmerei
Zielgruppe
Wir sind eine Zimmerei traditionell geprägte Zimmerei, die ihr Hauptaugenmerk auf Qualität und Zuverlässigkeit legt. Zur Zeit umfasst die Zimmerei Holger Brandt neben dem Inhaber zwei weitere Zimmerergesellen, einen Auszubildenden und einen Praktikanten.
Unsere Zielgruppe sind alle Personen- und Unternehmensgruppen in der nahen Umgebung, welche Zimmererarbeiten in Anspruch nehmen wollen.
Aufgabenstellung
Unsere Plakatwerbung soll vor allem Einfach und Übersichtlich gehalten werden.
Folgende Infos sollen dargestellt werden:
Zimmerei Holger Brandt
Aus dem Banner soll erstellt werden:
Baugerüstplanen: 200 cm x 205 cm
Bauzaunbanner: 340 cm x 173 cm
Schilder: 70 cm x 100 cm

```html
<!DOCTYPE html>
<html lang="de">
<head>
<meta charset="utf-8">
<title>Zimmerei Holger Brandt – Werbemittel</title>
<link rel="stylesheet" href="https://fonts.googleapis.com/css2?family=Roboto:wght@500;700&family=Roboto+Slab:wght@600;700;800&display=swap">
<style>
  :root {
    --brown-dark: #4a2c14;
    --brown: #6b4423;
    --brown-panel: #6e4624;
    --label: #7a5230;
    --gold: #ecbd78;
    --gold-soft: #f2cf96;
    --wood-1: #f6dcb4;
    --wood-2: #eccb98;
    --white: #ffffff;
  }
  * { margin: 0; padding: 0; box-sizing: border-box; }
  html, body { width: 981px; height: 1200px; overflow: hidden; background: var(--white); }
  body { position: relative; font-family: "Roboto", Arial, sans-serif; }

  .format-label {
    position: absolute; font-family: "Roboto", Arial, sans-serif; font-weight: 700;
    font-size: 20px; color: var(--label); transform: translateX(-50%); white-space: nowrap;
  }

  .sheet { position: absolute; overflow: hidden;
    background: linear-gradient(160deg, var(--wood-1) 0%, var(--wood-2) 55%, var(--wood-1) 100%); }
  .abs { position: absolute; }

  .photo-area { background: linear-gradient(150deg, #5a3b22 0%, #8a6442 45%, #4d321d 100%); }
  .panel { background: var(--brown-panel); }

  .title {
    position: absolute; left: 0; right: 0; text-align: center; white-space: nowrap;
    font-family: "Roboto Slab", Georgia, serif; font-weight: 800; color: var(--gold);
    text-shadow: 3px 3px 4px rgba(40,20,5,.55); line-height: 1;
  }
  .band {
    position: absolute; background: var(--brown-dark); color: var(--gold-soft);
    font-family: "Roboto Slab", Georgia, serif; font-weight: 600; text-align: center;
    white-space: nowrap; display: flex; align-items: center; justify-content: center;
    border-radius: 3px 10px 4px 12px;
  }
  .web-band {
    position: absolute; left: 0; right: 0; bottom: 0; background: var(--brown-dark);
    color: var(--gold); font-family: "Roboto Slab", Georgia, serif; font-weight: 700;
    display: flex; align-items: center; justify-content: center; white-space: nowrap;
  }

  .seal {
    position: absolute; border-radius: 50%; background: var(--white);
    border: 2px solid var(--brown-dark); display: flex; align-items: center;
    justify-content: center; text-align: center;
    font-family: "Roboto", Arial, sans-serif; font-weight: 700; color: var(--brown-dark);
    line-height: 1.15;
  }

  .contact { position: absolute; display: flex; align-items: center; color: var(--brown);
    font-weight: 500; white-space: nowrap; line-height: 1; }
  .contact svg { fill: var(--brown); flex: none; }

  .plane-art { position: absolute;
    background: radial-gradient(ellipse at 60% 70%, rgba(74,44,20,.55), rgba(74,44,20,.15) 70%, transparent 72%); }
</style>
</head>
<body>
<svg width="0" height="0" style="position:absolute">
  <defs>
    <symbol id="icon-pin" viewBox="0 0 24 24"><path d="M12 1a8 8 0 0 0-8 8c0 6 8 14 8 14s8-8 8-14a8 8 0 0 0-8-8zm0 11a3 3 0 1 1 0-6 3 3 0 0 1 0 6z"/></symbol>
    <symbol id="icon-phone" viewBox="0 0 24 24"><path d="M6.6 2.5l3 3.2-1.9 2.6c1.3 3 3.6 5.3 6.6 6.7l2.6-1.9 3.2 3-1.6 3.4C11 19.5 4.5 13 4 3.9z"/></symbol>
    <symbol id="icon-mobile" viewBox="0 0 24 24"><path d="M8 1h8a2 2 0 0 1 2 2v18a2 2 0 0 1-2 2H8a2 2 0 0 1-2-2V3a2 2 0 0 1 2-2zm0 2v16h8V3zm4 17.2a1 1 0 1 0 0 .1z" fill-rule="evenodd" transform="rotate(-25 12 12)"/></symbol>
    <symbol id="icon-mail" viewBox="0 0 24 24"><path d="M1 5h22v14H1zm2 2v.4l9 6 9-6V7zm0 2.8V17h18V9.8l-9 6z" fill-rule="evenodd"/></symbol>
  </defs>
</svg>

<!-- Baugerüstplane -->
<div class="format-label" style="left:295px; top:38px;">Baugerüstplane</div>
<section class="sheet scaffold-tarp" style="left:60px; top:87px; width:493px; height:506px;">
  <div class="abs photo-area" style="left:0; top:0; width:493px; height:261px;" role="img" aria-label="Foto eines Dachstuhls aus Holzbalken"></div>
  <div class="seal" style="left:200px; top:20px; width:96px; height:96px; font-size:13px;">Zimmerei<br>Holger<br>Brandt</div>
  <div class="title" style="top:133px; font-size:72px;">ZIMMEREI</div>
  <div class="title" style="top:203px; font-size:51px;">HOLGER BRANDT</div>
  <div class="band" style="left:65px; top:261px; width:375px; height:36px; font-size:19px;">Inh. Holger Brandt | Zimmerermeister</div>
  <div class="contact" style="left:20px; top:309px; font-size:23px;"><svg width="22" height="24"><use href="#icon-pin"/></svg><span style="margin-left:11px">Eichenweg 7 • 56068 Lindenau</span></div>
  <div class="contact" style="left:20px; top:350px; font-size:23px;"><svg width="22" height="24"><use href="#icon-phone"/></svg><span style="margin-left:11px">0261 / 55230</span></div>
  <div class="contact" style="left:20px; top:384px; font-size:23px;"><svg width="22" height="24"><use href="#icon-mobile"/></svg><span style="margin-left:11px">0171 / 5550123</span></div>
  <div class="contact" style="left:20px; top:420px; font-size:20px;"><svg width="22" height="22"><use href="#icon-mail"/></svg><span style="margin-left:11px">info@zimmerei-brandt.de</span></div>
  <div class="plane-art" style="left:310px; top:350px; width:170px; height:110px;" role="img" aria-label="Illustration eines Holzhobels"></div>
  <div class="web-band" style="height:54px; font-size:33px;">www.zimmerei-brandt.de</div>
</section>

<!-- Schild -->
<div class="format-label" style="left:765px; top:173px;">Schild</div>
<section class="sheet sign" style="left:635px; top:225px; width:258px; height:368px;">
  <div class="abs panel" style="left:0; top:27px; width:258px; height:186px;"></div>
  <div class="seal" style="left:100px; top:34px; width:66px; height:66px; font-size:9px;">Zimmerei<br>Holger<br>Brandt</div>
  <div class="title" style="top:115px; font-size:37px;">ZIMMEREI</div>
  <div class="title" style="top:152px; font-size:26px;">HOLGER BRANDT</div>
  <div class="band" style="left:20px; top:187px; width:220px; height:22px; font-size:11px;">Inh. Holger Brandt | Zimmerermeister</div>
  <div class="plane-art" style="left:30px; top:225px; width:200px; height:110px;" role="img" aria-label="Illustration eines Holzhobels"></div>
  <div class="web-band" style="height:30px; font-size:18px;">www.zimmerei-brandt.de</div>
</section>

<!-- Bauzaunbanner -->
<div class="format-label" style="left:242px; top:639px;">Bauzaunbanner</div>
<section class="sheet fence-banner" style="left:21px; top:674px; width:943px; height:480px;">
  <div class="abs panel" style="left:0; top:0; width:943px; height:154px;"></div>
  <div class="title" style="top:26px; font-size:62px;">ZIMMEREI HOLGER BRANDT</div>
  <div class="band" style="left:163px; top:96px; width:605px; height:56px; font-size:29px;">Inh. Holger Brandt | Zimmerermeister</div>
  <div class="seal" style="left:772px; top:99px; width:124px; height:124px; font-size:17px;">Zimmerei<br>Holger<br>Brandt</div>
  <div class="contact" style="left:38px; top:180px; font-size:36px;"><svg width="34" height="38"><use href="#icon-pin"/></svg><span style="margin-left:16px">Eichenweg 7 • 56068 Lindenau</span></div>
  <div class="contact" style="left:38px; top:254px; font-size:36px;"><svg width="34" height="38"><use href="#icon-phone"/></svg><span style="margin-left:16px">0261 / 55230</span></div>
  <div class="contact" style="left:38px; top:307px; font-size:36px;"><svg width="34" height="38"><use href="#icon-mobile"/></svg><span style="margin-left:16px">0171 / 5550123</span></div>
  <div class="contact" style="left:38px; top:363px; font-size:33px;"><svg width="36" height="34"><use href="#icon-mail"/></svg><span style="margin-left:16px">info@zimmerei-brandt.de</span></div>
  <div class="plane-art" style="left:580px; top:240px; width:340px; height:180px;" role="img" aria-label="Illustration eines Holzhobels"></div>
  <div class="web-band" style="height:69px; font-size:38px;">www.zimmerei-brandt.de</div>
</section>
</body>
</html>
```